Cool new eco friendly bamboo socks needs a flyer design & copy.

We need a flyer design for a Melbourne based ecommerce store. We have developed an innovative range of mens business socks, made from bamboo, a luxe fibre with great eco credentials.
Flyer to be horizontal. Design to be modern, uncluttered, minimal imagery.
Front.
www.Plimvale.com.au - bold heading.
image set up and layout to mimic homepage on web site - with pick a pair or work week imagery and layout.
At the bottom of the front page - please insert "All truly great thoughts are concieved by walking" Ludwig Brandauer.
Back.
Please insert bamboo image to run horizintal at top.

wrods;
Did you know?
- Bamboo is decadently soft and silky.
-Bamboo is particularly absorbent, able to thermo regulate, keeping feet warm in winter & cool in summer.
-Bamboo has natural antibacterial properties - stinky feet no more!

Bottom heading
Luxe bamboo business socks
secondary heading:
put your feet up- we'll deliver them to your door.

Target Market(s)

Business men 40+

Industry/Entity Type

Business

Requirements
Must have
• Horizontal layout
minimal and modern so imagery is hero
Font must be F25 executive
Should not have
• clutter

```html
<!DOCTYPE html>
<html lang="en">
<head>
<meta charset="utf-8">
<title>Plimvale Bamboo Socks Flyer</title>
<link rel="stylesheet" href="https://fonts.googleapis.com/css2?family=Kreon:wght@400;700&family=Cutive&display=swap">
<style>
  :root {
    --stage: #000000;
    --paper-top: #ffffff;
    --paper-bottom: #efefef;
    --ink: #111111;
    --blue: #4a96c4;
    --orange: #e8543a;
    --red: #e24a36;
    --green: #2f6a2a;
    --bamboo-dark: #4f8f2a;
    --bamboo-light: #a6d46a;
    --sock-dark: #141414;
    --sock-mid: #2c2c2c;
  }
  * { margin: 0; padding: 0; box-sizing: border-box; }
  html, body {
    width: 1076px; height: 1200px; overflow: hidden;
    background: var(--stage);
  }
  .canvas { position: relative; width: 1076px; height: 1200px; }
  .side {
    position: absolute; left: 54px; width: 974px; height: 472px;
    background: linear-gradient(180deg, var(--paper-top) 0%, var(--paper-top) 55%, var(--paper-bottom) 100%);
    overflow: hidden;
    font-family: "Cutive", "Courier New", serif;
    color: var(--ink);
  }
  .side--front { top: 81px; }
  .side--back { top: 648px; }

  .web-heading {
    position: absolute; top: 30px; left: 0; width: 100%;
    text-align: center; font-family: "Kreon", serif; font-weight: 700;
    font-size: 46px; letter-spacing: 1px;
  }
  .sock-photo {
    position: absolute; border-radius: 14px;
    background: linear-gradient(160deg, var(--sock-mid), var(--sock-dark));
  }
  .sock-photo--pair { left: 121px; top: 112px; width: 150px; height: 238px; }
  .sock-photo--week { left: 625px; top: 112px; width: 230px; height: 238px; }
  .pack-bar {
    position: absolute; top: 205px; height: 30px;
    color: #fff; font-size: 16px; letter-spacing: 1px;
    display: flex; align-items: center; padding: 0 12px;
  }
  .pack-bar--pair { left: 128px; width: 347px; background: var(--blue); justify-content: flex-end; }
  .pack-bar--week { left: 524px; width: 330px; background: var(--orange); }
  .pack-or {
    position: absolute; left: 483px; top: 208px; font-size: 18px;
  }
  .quote {
    position: absolute; top: 384px; left: 0; width: 100%; text-align: center;
    font-size: 18px;
  }
  .quote-author {
    position: absolute; top: 413px; left: 0; width: 100%; text-align: center;
    font-size: 17px; color: var(--red);
  }

  .bamboo-photo {
    position: absolute; left: 0; top: 0; width: 100%; height: 86px;
    background: linear-gradient(90deg, var(--bamboo-dark), var(--bamboo-light) 20%, var(--bamboo-dark) 40%, var(--bamboo-light) 60%, var(--bamboo-dark) 80%, var(--bamboo-light));
  }
  .brand-name {
    position: absolute; left: 660px; top: 126px;
    font-family: "Kreon", serif; font-weight: 400; font-size: 50px; letter-spacing: 1px;
  }
  .facts-title {
    position: absolute; left: 138px; top: 162px;
    font-size: 27px; color: var(--green);
  }
  .facts { position: absolute; left: 138px; top: 210px; width: 640px; list-style: none; }
  .facts li {
    position: relative; font-size: 17px; line-height: 20px;
    padding-left: 8px; margin-bottom: 15px;
  }
  .facts li::before {
    content: ""; position: absolute; left: -2px; top: 7px;
    width: 4px; height: 4px; background: var(--red);
  }
  .range-heading {
    position: absolute; left: 138px; top: 360px;
    font-size: 31px; color: var(--blue); letter-spacing: 1px;
  }
  .delivery-line {
    position: absolute; left: 138px; top: 398px;
    font-size: 24px; color: var(--red);
  }
</style>
</head>
<body>
<main class="canvas">
  <section class="side side--front">
    <h1 class="web-heading">www.plimvale.com.au</h1>
    <div class="sock-photo sock-photo--pair" role="img" aria-label="Photo of a pair of black bamboo business socks with blue heel"></div>
    <div class="sock-photo sock-photo--week" role="img" aria-label="Photo of black bamboo socks with orange heel and a stack of five colourful toe packs"></div>
    <div class="pack-bar pack-bar--pair">PICK-A-PAIR</div>
    <span class="pack-or">OR</span>
    <div class="pack-bar pack-bar--week">WORK WEEK PACK</div>
    <p class="quote">"All truly great thoughts are concieved by walking"</p>
    <p class="quote-author">Ludwig Brandauer</p>
  </section>

  <section class="side side--back">
    <div class="bamboo-photo" role="img" aria-label="Photo of green bamboo stalks"></div>
    <div class="brand-name">PLIMVALE</div>
    <h2 class="facts-title">Did you know?</h2>
    <ul class="facts">
      <li>Bamboo is decadently soft and silky.</li>
      <li>Bamboo is particularly absorbent, able to thermo regulate,<br>keeping feet warm in winter &amp; cool in summer.</li>
      <li>Bamboo has natural antibacterial properties - stinky feet no more!</li>
    </ul>
    <h3 class="range-heading">LUXE BAMBOO BUSINESS SOCKS</h3>
    <p class="delivery-line">Put your feet up- we'll deliver them to your door</p>
  </section>
</main>
</body>
</html>
```